International freight forwarder experienced in perishable handling needs a web design

We need a website designed that will allow us to capture more customers through the website. We would like a visually appealing design that is not so heavy on text. Our business covers the logistics and freight forwarding industries and we have offices in South America and the USA. Our main customers are importers USA, Europe, Asia and Russia and we currently work almost exclusively with perishable products such as fresh cut flowers, fresh exotics fruits, cacao, fresh fish etc. We would like to convey a fresh, modern approach to freight forwarding focusing on concepts such as - time sensitive, anytime-anywhere delivery, innovation, experience, reliability and confidence. Should include links with Plumetta and Worvanet. Our core solutions include: Core Services
*Air Freight
*Ocean Freight
*Warehousing & Distribution
Our industry solutions cover
*Flowers
*FMCG including, fruits, vegetables
*Live animals
*Automotive
*Consumer Goods
*Industrial
*Oil & Gas
*Pharma
* Event logistics
* Project logistics

Target Market(s)

Importers in Europe, USA, Asia, Middle East and Russia

Number of Pages Required

4 page

Font styles to use
Sans Serif

Colors
a1cd39
606060
000000

Requirements
Must have
• Photos of fresh cut flowers, FMCG such as cacao, fresh fish (packaged for shipping), fresh exotic fruits, pharma products (packaged for shipping), oil and gas etc. Internal customer login access
Nice to have
• Photos of cargo shipping carriers and cargo airline carriers. Features similar to those of following website http://www.brolvacargo.com/eng/main/index.jsp?FromURL=web
Should not have
• Too much text, needs to be visually pleasing

```html
<!DOCTYPE html>
<html lang="en">
<head>
<meta charset="utf-8">
<title>Fennrow Alliance Group – Freight Services</title>
<link href="https://fonts.googleapis.com/css2?family=Roboto+Condensed:wght@400;700&family=Open+Sans:ital,wght@0,400;0,700;1,400&display=swap" rel="stylesheet">
<style>
:root{
  --green:#a1cd39;
  --green-dark:#6f9a1e;
  --grey:#606060;
  --ink:#1e1e1e;
  --dark:#2a2a2a;
  --paper:#ffffff;
  --muted:#8a8a8a;
}
*{box-sizing:border-box;margin:0;padding:0}
html,body{width:774px;height:1200px;overflow:hidden;background:var(--paper)}
body{position:relative;font-family:"Open Sans",Arial,sans-serif;color:var(--grey)}
.cond{font-family:"Roboto Condensed","Arial Narrow",sans-serif}
.abs{position:absolute}
a{color:inherit;text-decoration:none}

/* top nav */
.top-nav{position:absolute;left:0;top:0;width:774px;height:16px;background:linear-gradient(#fafafa,#e6e6e6);
  display:flex;justify-content:center;align-items:center;gap:6px;font:700 6.4px "Roboto Condensed",sans-serif;color:#333;text-transform:uppercase}
.top-nav .sep{color:var(--green)}
.header{position:absolute;left:0;top:16px;width:774px;height:42px;background:#fff}
.follow{position:absolute;left:174px;top:15px;display:flex;align-items:center;gap:4px;font:700 6.4px "Roboto Condensed",sans-serif;color:#333}
.follow .lbl span{color:var(--green)}
.social{font:700 6px "Roboto Condensed",sans-serif;color:#fff;background:var(--grey);border-radius:8px;padding:2px 5px}
.brand{position:absolute;left:315px;top:8px;width:144px;height:34px;display:flex;flex-direction:column;align-items:center;justify-content:center}
.brand-name{font:700 15px "Roboto Condensed",sans-serif;color:#444;display:flex;align-items:center;gap:5px}
.brand-name i{display:inline-block;width:14px;height:14px;border-radius:50%;background:var(--green)}
.brand-sub{font:400 5px "Open Sans",sans-serif;letter-spacing:2px;color:#999;margin-left:40px}
.tools{position:absolute;left:516px;top:9px;display:flex;gap:4px}
.pill{height:20px;border:1.5px solid var(--green);border-radius:10px;font:700 6.4px "Roboto Condensed",sans-serif;color:#333;display:flex;align-items:center;justify-content:center;padding:0 7px}
.pill.round{width:20px;padding:0}

/* hero */
.hero{position:absolute;left:0;top:58px;width:774px;height:278px;background:linear-gradient(180deg,#8fb4d6 0%,#cfdce8 45%,#8f8a82 75%,#6e6d6a 100%)}
.hero-kicker{position:absolute;top:33px;width:100%;text-align:center;font:700 10px "Roboto Condensed",sans-serif;color:var(--green)}
.hero-title{position:absolute;top:50px;width:100%;text-align:center;font:700 21px/20px "Roboto Condensed",sans-serif;color:#333}
.service{position:absolute;top:139px;width:134px;height:117px;background:rgba(120,170,40,.92);padding:13px 15px;color:#fff}
.service h3{font:700 10px/9px "Roboto Condensed",sans-serif;text-transform:uppercase;margin-bottom:9px}
.service p{font-size:5px;line-height:8px;height:40px}
.btn{display:inline-block;border:1px solid currentColor;font:700 6px "Open Sans",sans-serif;padding:3px 8px}
.service .btn{margin-top:9px;border-color:#fff;color:#fff}

/* industries */
.industries{position:absolute;left:0;top:336px;width:774px;height:263px;background:radial-gradient(ellipse at center,#3a3a3a 0%,#262626 70%,#1e1e1e 100%)}
.sec-title{position:absolute;width:100%;text-align:center;font:700 16px "Roboto Condensed",sans-serif}
.rule{position:absolute;left:330px;width:114px;height:6px}
.ind-card{position:absolute;top:94px;width:123px;height:119px;border:1px solid var(--green);padding:9px 10px 0 25px;color:#ddd}
.ind-card h3{font:700 8px/8px "Roboto Condensed",sans-serif;color:var(--green);text-transform:uppercase;margin-bottom:6px}
.ind-card p{font-size:4.8px;line-height:8px;height:72px}
.ind-card .btn{color:#fff;border-color:#fff;margin-top:2px}
.ind-icon{position:absolute;left:9px;top:8px;width:12px;height:12px}
.dots{position:absolute;width:100%;display:flex;justify-content:center;gap:2px}
.dots i{width:4px;height:4px;border-radius:50%;background:#fff;display:block}
.dots i.off{background:transparent;border:1px solid #fff}

/* testimonial */
.testimonial{position:absolute;left:0;top:599px;width:774px;height:251px;background:radial-gradient(ellipse at 50% 40%,#8cc43c 0%,#6fa528 60%,#5f9420 100%)}
.portrait{position:absolute;left:354px;top:67px;width:66px;height:64px;border:2px solid #3b3b3b;background:linear-gradient(#5a7aa6,#9b8873)}
.quote{position:absolute;left:238px;top:142px;width:298px;text-align:center;font:italic 400 6px/8.8px "Open Sans",sans-serif;color:#1d2a0a}
.who{position:absolute;top:200px;width:100%;text-align:center;font:700 7px "Roboto Condensed",sans-serif;color:#222}
.role{position:absolute;top:210px;width:100%;text-align:center;font-size:5px;color:#222}

/* news */
.news{position:absolute;left:0;top:850px;width:774px;height:196px;background:#fff}
.news-title{position:absolute;top:21px;width:100%;text-align:center;font:700 18px "Roboto Condensed",sans-serif;color:var(--ink)}
.news-sub{position:absolute;top:42px;width:100%;text-align:center;font-size:6.5px;color:#333}
.post{position:absolute;top:73px;width:136px}
.post h3{font:400 11.5px/13px "Roboto Condensed",sans-serif;color:#333;text-transform:uppercase;margin-bottom:6px}
.post p{font-size:4.8px;line-height:8px;color:var(--muted);height:40px}
.post .btn{color:#333;border-color:#777;margin-top:8px}

/* footer */
.footer{position:absolute;left:0;top:1046px;width:774px;height:154px;background:linear-gradient(#262626,#1c1c1c);color:#ccc}
.f-head{position:absolute;top:26px;font:700 7px "Roboto Condensed",sans-serif;color:var(--green);text-transform:uppercase}
.f-brand{position:absolute;left:174px;top:49px;font:700 12px "Roboto Condensed",sans-serif;color:#fff;display:flex;align-items:center;gap:4px}
.f-brand i{width:14px;height:14px;border-radius:50%;background:#fff;display:block}
.f-about{position:absolute;left:174px;top:78px;width:136px;font-size:5px;line-height:8px;color:#fff}
.f-links{position:absolute;left:352px;top:48px;list-style:none;font:5px/9.2px "Open Sans",sans-serif;color:#fff;text-transform:uppercase}
.f-links li::before{content:"• ";color:var(--green)}
.f-contact{position:absolute;left:466px;top:48px;font-size:5px;line-height:11px;color:#fff}
.f-contact span{color:var(--green)}
.newsletter{position:absolute;left:466px;top:91px;font:700 7px "Roboto Condensed",sans-serif;color:#fff}
.nl-form{position:absolute;left:466px;top:92px;width:134px;height:14px;border:1px solid var(--green);display:flex;font-size:5px;margin-top:10px}
.nl-form .field{flex:1;color:#fff;padding:3px 5px}
.nl-form .go{width:39px;border-left:1px solid var(--green);color:var(--green);padding:3px 6px}
.copy{position:absolute;left:174px;top:134px;font-size:5px;color:#fff}
.copy span{color:var(--green)}
</style>
</head>
<body>

<nav class="top-nav">
  <a>Our Company</a><span class="sep">/</span>
  <a>Freight Forwarding Services</a><span class="sep">/</span>
  <a>Industry Specific Solutions</a><span class="sep">/</span>
  <a>Express</a><span class="sep">/</span>
  <a>Innovation</a><span class="sep">/</span>
  <a>Contact Us</a>
</nav>

<header class="header">
  <div class="follow">
    <span class="lbl">FOLLOW <span>US</span></span>
    <a class="social">Plumetta</a><a class="social">Chirpwell</a><a class="social">Worvanet</a>
  </div>
  <div class="brand">
    <div class="brand-name"><i></i>Fennrow Alliance</div>
    <div class="brand-sub">GROUP</div>
  </div>
  <div class="tools">
    <a class="pill">LOGIN
      <svg width="7" height="7" viewBox="0 0 10 10" style="margin-left:3px"><circle cx="3.5" cy="3.5" r="2.5" fill="none" stroke="#a1cd39" stroke-width="1.5"/><path d="M5 5l4 4M7 7l1.5-1" stroke="#a1cd39" stroke-width="1.5"/></svg>
    </a>
    <a class="pill round"><svg width="7" height="7" viewBox="0 0 10 10"><circle cx="4" cy="4" r="3" fill="none" stroke="#666" stroke-width="1.3"/><path d="M6.3 6.3L9 9" stroke="#666" stroke-width="1.3"/></svg></a>
    <a class="pill round"><svg width="12" height="7" viewBox="0 0 12 7"><rect width="7" height="5" y="1" fill="#b22"/><rect width="3" height="2.5" y="1" fill="#226"/><path d="M9 3l1.5 1.5L12 3z" fill="#555"/></svg></a>
  </div>
</header>

<section class="hero">
  <div class="abs" role="img" aria-label="Cargo airliner being loaded with palletised freight on an airport apron" style="inset:0;background:linear-gradient(180deg,rgba(143,180,214,.6),rgba(210,215,220,.4) 50%,rgba(110,108,104,.7))"></div>
  <div class="hero-kicker">BUSINESS TO FENNROW ALLIANCE GROUP</div>
  <h1 class="hero-title">PROVIDING FIRST CLASS<br>FREIGHT SERVICES</h1>

  <article class="service" style="left:174px">
    <h3>Air Freight</h3>
    <p>Lorem Ipsum has been the industry's standard dummy text ever since the 1500s, when an unknown printer took a galley of type and scrambled it to make a type specimen book.</p>
    <a class="btn">Read More</a>
  </article>
  <article class="service" style="left:320px">
    <h3>Ocean Freight</h3>
    <p>Lorem Ipsum has been the industry's standard dummy text ever since the 1500s, when an unknown printer took a galley of type and scrambled it to make a type specimen book.</p>
    <a class="btn">Read More</a>
  </article>
  <article class="service" style="left:466px">
    <h3>Warehousing<br>&amp; Distribution</h3>
    <p style="height:31px">Lorem Ipsum has been the industry's standard dummy text ever since the 1500s, when an unknown printer took a galley of type and scrambled it to make a type</p>
    <a class="btn">Read More</a>
  </article>
</section>

<section class="industries">
  <div class="abs" role="img" aria-label="Faint world map with network circles in the background" style="inset:0;background:radial-gradient(ellipse at 50% 55%,rgba(80,80,80,.25),rgba(0,0,0,0) 60%)"></div>
  <h2 class="sec-title" style="top:35px;color:#fff">OUR INDUSTRY SOLUTIONS COVER</h2>
  <svg class="rule" style="top:56px" viewBox="0 0 114 6"><path d="M0 1 L57 5 L114 1" fill="none" stroke="#a1cd39" stroke-width="1"/></svg>

  <svg class="abs" style="left:165px;top:144px" width="10" height="20" viewBox="0 0 10 20"><path d="M9 1L1 10l8 9" fill="none" stroke="#a1cd39" stroke-width="1.2"/></svg>
  <svg class="abs" style="left:600px;top:144px" width="10" height="20" viewBox="0 0 10 20"><path d="M1 1l8 9-8 9" fill="none" stroke="#a1cd39" stroke-width="1.2"/></svg>

  <article class="ind-card" style="left:186px">
    <svg class="ind-icon" viewBox="0 0 12 12"><path d="M6 11V6M3 2c0 3 1.5 4 3 4s3-1 3-4C8 3 7 3 6 1 5 3 4 3 3 2z" fill="none" stroke="#a1cd39"/></svg>
    <h3>Flowers</h3>
    <p>Lorem ipsum dolor sit amet, consectetur adipisicing elit, sed do eiusmod tempor incididunt ut labore et dolore magna aliqua. Ut enim ad minim veniam, quis nostrud exercitation ullamco laboris nisi ut aliquip ex ea commodo consequat. Duis aute irure dolor in reprehenderit in voluptate velit esse cillum.</p>
    <a class="btn">Read More</a>
  </article>
  <article class="ind-card" style="left:326px">
    <svg class="ind-icon" viewBox="0 0 12 12"><path d="M1 11C4 9 9 6 10 2M10 2L8 1M10 2l1 2" fill="none" stroke="#a1cd39"/></svg>
    <h3>FMCG including,<br>fruits, vegetables</h3>
    <p style="height:64px">Lorem ipsum dolor sit amet, consectetur adipisicing elit, sed do eiusmod tempor incididunt ut labore et dolore magna aliqua. Ut enim ad minim veniam, quis nostrud exercitation ullamco laboris nisi ut aliquip ex ea commodo consequat. Duis aute irure dolor in reprehenderit.</p>
    <a class="btn">Read More</a>
  </article>
  <article class="ind-card" style="left:466px">
    <svg class="ind-icon" viewBox="0 0 12 12"><circle cx="6" cy="8" r="2.5" fill="none" stroke="#a1cd39"/><circle cx="2" cy="5" r="1.2" fill="none" stroke="#a1cd39"/><circle cx="10" cy="5" r="1.2" fill="none" stroke="#a1cd39"/><circle cx="4.3" cy="2" r="1.2" fill="none" stroke="#a1cd39"/><circle cx="7.7" cy="2" r="1.2" fill="none" stroke="#a1cd39"/></svg>
    <h3>Live Animals</h3>
    <p>Lorem ipsum dolor sit amet, consectetur adipisicing elit, sed do eiusmod tempor incididunt ut labore et dolore magna aliqua. Ut enim ad minim veniam, quis nostrud exercitation ullamco laboris nisi ut aliquip ex ea commodo consequat. Duis aute irure dolor in reprehenderit.</p>
    <a class="btn">Read More</a>
  </article>

  <div class="dots" style="top:223px"><i></i><i class="off"></i><i></i><i></i><i></i></div>
</section>

<section class="testimonial">
  <h2 class="sec-title" style="top:35px;color:#fff">WHAT CUSTOMERS ARE SAYING ABOUT US</h2>
  <svg class="rule" style="top:58px" viewBox="0 0 114 6"><path d="M0 1 L57 5 L114 1" fill="none" stroke="#fff" stroke-width="1"/></svg>
  <div class="portrait" role="img" aria-label="Portrait photo of the customer quoted"></div>
  <p class="quote">What can we say but thank you to Kestrel Labs and Orbin Networks, they were able to quickly and effectively solve our WiFi problems. We had a very tight schedule to meet and they were able to get the results we needed. Now, several weeks later, we have logged more users and bandwidth usage on the network than ever before. As a result, site management has noted a dramatic decrease in the number of resident complaints or issues with wireless connectivity. Today, the network handles hundreds of bandwidth hungry college students - impossible with the old WiFi system.</p>
  <div class="who">-ALAN DREWER</div>
  <div class="role">DIRECTOR OF CAPITAL PROJECTS AND FINANCE</div>
  <div class="dots" style="top:232px"><i></i><i class="off"></i><i></i><i></i><i></i></div>
</section>

<section class="news">
  <h2 class="news-title">LATEST NEWS</h2>
  <div class="news-sub">STAY TUNED</div>
  <article class="post" style="left:174px">
    <h3>What Customers<br>Time Sensitive</h3>
    <p>Lorem ipsum dolor sit amet, consectetur adipisicing elit, sed do eiusmod tempor incididunt ut labore et dolore magna aliqua. Ut enim ad minim veniam, quis nostrud exercitation ullamco laboris nisi ut aliquip ex ea commodo consequat.</p>
    <a class="btn">Read More</a>
  </article>
  <article class="post" style="left:320px">
    <h3>What Customers<br>Time Sensitive</h3>
    <p>Lorem ipsum dolor sit amet, consectetur adipisicing elit, sed do eiusmod tempor incididunt ut labore et dolore magna aliqua. Ut enim ad minim veniam, quis nostrud exercitation ullamco laboris nisi ut aliquip ex ea commodo consequat.</p>
    <a class="btn">Read More</a>
  </article>
  <article class="post" style="left:466px">
    <h3>Confidenceare<br>Saying About Us</h3>
    <p>Lorem ipsum dolor sit amet, consectetur adipisicing elit, sed do eiusmod tempor incididunt ut labore et dolore magna aliqua. Ut enim ad minim veniam, quis nostrud exercitation ullamco laboris nisi ut aliquip ex ea commodo consequat.</p>
    <a class="btn">Read More</a>
  </article>
</section>

<footer class="footer">
  <div class="abs" role="img" aria-label="Dark photo of a warehouse with stacked cargo" style="inset:0;background:linear-gradient(160deg,rgba(60,60,60,.35),rgba(0,0,0,0) 60%)"></div>
  <h4 class="f-head" style="left:174px">About Our Company</h4>
  <h4 class="f-head" style="left:352px">Useful Links</h4>
  <h4 class="f-head" style="left:466px">Contact Info</h4>

  <div class="f-brand"><i></i>Fennrow Alliance</div>
  <p class="f-about">Lorem ipsum dolor sit amet, consectetur adipisicing elit, sed do eiusmod tempor incididunt ut labore et dolore magna aliqua. Ut enim ad minim veniam, quis nostrud exercitation ullamco.</p>

  <ul class="f-links">
    <li>Our Company</li><li>Freight Forwarding Services</li><li>Industry Specific Solutions</li>
    <li>Express</li><li>Innovation</li><li>Contact Us</li>
  </ul>

  <div class="f-contact">
    <div><span>Address</span> : Harlow Court, 12 Mill Lane, Leeds</div>
    <div><span>Phone Number</span> : +44 20 0000 4417</div>
  </div>
  <div class="newsletter">NEWSLETTER</div>
  <div class="nl-form"><span class="field">Address Email</span><span class="go">Subscribe</span></div>

  <div class="copy"><span>2015 FENNROW ALLIANCE</span> - All Rights Reserved</div>
</footer>

</body>
</html>
```